The Marrowby Doctrines book cover design [front and back covers]

I need a book cover design for a trade book called THE MARROWBY DOCTRINES.

Cover Title: the Marrowby Doctrines
Subheading: The business wisdom of Dominic Ravell, a successful Australian entrepreneur.

NOTE: I originally posted this contest with 2 authors. I NOW ONLY WANT TO HAVE ONE AUTHORS NAME ON THE BOOK. Author: Dominic Ravell

It's about the business principals that has made this man so successful.

The man this book is about owns a company called Cobalt Rentals and their colour is red. So I'd like the cover to have a strong red influence. I've included his logo and other samples of their branding.

I'd like the book design to look like a Harbourline Ledger best seller style book. Sophisticated and simple. I'd like it to be clear that this book comes from the same man that built Cobalt rentals, but I don't want it to look like a corporate brochure. It must look like a book you would see at the airport book shop.

I've also included some book cover inspiration to give you an idea of the direction I'd like for this design.

```html
<!DOCTYPE html>
<html lang="en">
<head>
<meta charset="utf-8">
<title>The Marrowby Doctrines – Cover Concepts</title>
<link rel="stylesheet" href="https://fonts.googleapis.com/css2?family=Oswald:wght@300;400;500&family=Playfair+Display:wght@400&family=Lora:ital@1&family=Pinyon+Script&display=swap">
<style>
  :root {
    --sheet: #dcd7d3;
    --red: #d60d0d;
    --deep-red: #a10d0d;
    --charcoal: #333335;
    --ink: #141414;
    --white: #ffffff;
    --gold: #f2c318;
    --paper: #f4f4f4;
    --navy: #1f2a7a;
    --brass: #c9a23a;
  }
  * { box-sizing: border-box; margin: 0; padding: 0; }
  html, body { width: 758px; height: 1200px; overflow: hidden; }
  body { background: var(--sheet); position: relative; font-family: "Oswald", sans-serif; }

  .cover { position: absolute; width: 316px; height: 500px; overflow: hidden; }
  .cover--red { left: 30px; top: 48px; }
  .cover--city { left: 410px; top: 48px; }
  .cover--leather { left: 30px; top: 665px; }
  .cover--flag { left: 410px; top: 665px; }

  .spine {
    position: absolute; left: 0; top: 0; bottom: 0; width: 22px;
    display: flex; flex-direction: column; align-items: center;
    border-right: 1px solid rgba(0,0,0,.25);
  }
  .spine-title, .spine-author {
    writing-mode: vertical-rl; font-family: "Oswald", sans-serif;
    font-size: 10px; letter-spacing: .5px; white-space: nowrap;
  }
  .spine-title { margin-top: 50px; font-style: italic; font-weight: 500; }
  .spine-author { margin-top: auto; margin-bottom: 14px; font-size: 8px; line-height: 1.1; }
  .front { position: absolute; left: 22px; top: 0; right: 0; bottom: 0; }

  /* Cover 1 – red */
  .cover--red .front { background: var(--red); }
  .cover--red .spine { background: linear-gradient(var(--red) 84%, var(--charcoal) 84%); color: var(--ink); }
  .cover--red .spine-author { color: var(--paper); }
  .cover--red .subtitle {
    position: absolute; top: 38px; left: 40px; right: 14px; color: var(--white);
    font-family: "Playfair Display", serif; font-size: 8px; text-align: center; line-height: 1.35;
  }
  .cover--red .rule { position: absolute; top: 76px; right: 20px; width: 38px; height: 2px; background: var(--white); }
  .cover--red .tag { position: absolute; top: 128px; left: 62px; color: var(--white); font-family: "Lora", serif; font-style: italic; font-size: 9px; }
  .cover--red .chart { position: absolute; top: 150px; left: 36px; }
  .cover--red .title {
    position: absolute; top: 150px; right: 18px; color: var(--white); text-align: right;
    font-weight: 400; font-size: 48px; line-height: 1.1;
  }
  .cover--red .band { position: absolute; left: 0; right: 0; bottom: 0; height: 80px; background: var(--charcoal); border-top: 4px solid var(--white); }
  .cover--red .author { position: absolute; bottom: 46px; right: 30px; color: var(--gold); font-family: "Playfair Display", serif; font-size: 12px; }

  /* Cover 2 – city */
  .cover--city .spine { background: linear-gradient(#5b5b5b 0%, #8a8a8a 30%, #c9c9c9 60%, var(--charcoal) 60%); color: var(--deep-red); }
  .cover--city .spine-author { color: var(--gold); }
  .cover--city .front { background: var(--charcoal); }
  .cover--city .photo { position: absolute; left: 0; top: 0; right: 0; height: 330px; background: linear-gradient(#3c3c3c, #9a9a9a 55%, #e6e6e6 85%, #3a3a3a); }
  .cover--city .title-box {
    position: absolute; left: 44px; right: 26px; top: 310px; height: 62px; background: var(--red);
    border: 2px solid var(--gold); display: flex; flex-direction: column; align-items: center; justify-content: center;
    color: var(--paper); font-weight: 300; font-size: 20px; line-height: 1.05; text-align: center;
  }
  .cover--city .subtitle { position: absolute; top: 382px; left: 40px; right: 20px; color: var(--gold); font-family: "Playfair Display", serif; font-size: 7.5px; text-align: center; line-height: 1.3; }
  .cover--city .author { position: absolute; top: 418px; left: 0; right: 0; color: #e8e8e8; text-align: center; font-family: "Playfair Display", serif; font-size: 18px; }

  /* Cover 3 – leather */
  .cover--leather .spine { background: var(--ink); color: var(--white); }
  .cover--leather .front { background: #1b1b1b; }
  .cover--leather .stitch { position: absolute; inset: 6px 8px; border-left: 1px dashed #555; border-right: 1px dashed #555; }
  .cover--leather .subtitle { position: absolute; top: 60px; left: 30px; right: 20px; color: var(--white); font-size: 10px; font-weight: 400; text-align: center; line-height: 1.35; }
  .cover--leather .flourish { position: absolute; left: 92px; width: 110px; height: 8px; background: var(--brass); }
  .cover--leather .flourish--top { top: 126px; }
  .cover--leather .flourish--bottom { top: 342px; }
  .cover--leather .title { position: absolute; top: 150px; left: 0; right: 0; color: #e9e9e9; text-align: center; font-weight: 500; font-size: 44px; line-height: 1.12; }
  .cover--leather .author { position: absolute; top: 396px; left: 0; right: 0; color: #b30f0f; text-align: center; font-family: "Pinyon Script", cursive; font-size: 26px; }

  /* Cover 4 – flag */
  .cover--flag .spine { background: linear-gradient(var(--paper) 52%, var(--charcoal) 52%); color: var(--deep-red); }
  .cover--flag .spine-author { color: var(--gold); }
  .cover--flag .front { background: linear-gradient(var(--paper) 52%, var(--charcoal) 52%); }
  .cover--flag .frame { position: absolute; inset: 26px 18px 26px 20px; border: 1px solid var(--ink); }
  .cover--flag .map { position: absolute; left: 44px; top: 40px; width: 228px; height: 190px; background: var(--navy); border-radius: 30% 40% 35% 45%; }
  .cover--flag .title-box { position: absolute; left: 34px; top: 220px; width: 200px; height: 110px; background: var(--deep-red); padding: 10px 0 0 14px; color: var(--white); font-weight: 400; font-size: 25px; line-height: 1.1; letter-spacing: 1px; }
  .cover--flag .subtitle { position: absolute; top: 344px; left: 48px; right: 40px; color: var(--gold); font-size: 7px; line-height: 1.5; }
  .cover--flag .rule { position: absolute; top: 376px; left: 48px; width: 34px; height: 2px; background: var(--white); }
  .cover--flag .author { position: absolute; top: 388px; left: 48px; color: var(--white); font-size: 11px; font-weight: 300; }

  .sheet-note { position: absolute; top: 578px; left: 0; right: 0; text-align: center; font-family: "Oswald", sans-serif; font-weight: 500; font-size: 30px; color: var(--ink); letter-spacing: .5px; }
</style>
</head>
<body>

<section class="cover cover--red">
  <div class="spine"><span class="spine-title">THE MARROWBY DOCTRINES</span><span class="spine-author">DOMINIC RAVELL</span></div>
  <div class="front">
    <p class="subtitle">THE BUSINESS WISDOM OF DOMINIC RAVELL, A SUCCESSFUL AUSTRALIAN ENTREPRENEUR</p>
    <span class="rule"></span>
    <p class="tag">The best book</p>
    <svg class="chart" width="100" height="60" viewBox="0 0 100 60">
      <polyline points="8,52 26,26 44,34 62,12 88,6" fill="none" stroke="#f2c318" stroke-width="3"/>
      <g fill="#f2c318"><circle cx="8" cy="52" r="5"/><circle cx="26" cy="26" r="5"/><circle cx="44" cy="34" r="5"/><circle cx="88" cy="6" r="5"/></g>
    </svg>
    <h1 class="title">The<br>Marrowby<br>Doctrines</h1>
    <div class="band"></div>
    <p class="author">Dominic Ravell</p>
  </div>
</section>

<section class="cover cover--city">
  <div class="spine"><span class="spine-title">THE MARROWBY DOCTRINES</span><span class="spine-author">DOMINIC RAVELL</span></div>
  <div class="front">
    <div class="photo" role="img" aria-label="Aerial photo of city towers with a lone figure standing on a ledge"></div>
    <h1 class="title-box"><span>THE</span><span>MARROWBY DOCTRINES</span></h1>
    <p class="subtitle">THE BUSINESS WISDOM OF DOMINIC RAVELL, A SUCCESSFUL AUSTRALIAN ENTREPRENEUR</p>
    <p class="author">DOMINIC RAVELL</p>
  </div>
</section>

<p class="sheet-note">FULL SIZE COVERS ARE ATTACHED</p>

<section class="cover cover--leather">
  <div class="spine"><span class="spine-title">THE MARROWBY DOCTRINES</span></div>
  <div class="front">
    <div class="stitch"></div>
    <p class="subtitle">The business wisdom of dominic ravell, a successful australian entrepreneur</p>
    <div class="flourish flourish--top" role="img" aria-label="Gold ornamental flourish"></div>
    <h1 class="title">THE<br>MARROWBY<br>DOCTRINES</h1>
    <div class="flourish flourish--bottom" role="img" aria-label="Gold ornamental flourish"></div>
    <p class="author">Dominic Ravell</p>
  </div>
</section>

<section class="cover cover--flag">
  <div class="spine"><span class="spine-title">THE MARROWBY DOCTRINES</span><span class="spine-author">DOMINIC RAVELL</span></div>
  <div class="front">
    <div class="frame"></div>
    <div class="map" role="img" aria-label="Map of Australia filled with the Australian flag"></div>
    <h1 class="title-box">THE<br>MARROWBY<br>DOCTRINES</h1>
    <p class="subtitle">The business wisdom of dominic ravell, a successful australian entrepreneur</p>
    <span class="rule"></span>
    <p class="author">DOMINIC RAVELL</p>
  </div>
</section>

</body>
</html>
```